Company letter head and business card for new Indian Pharmaceutical Export company.

We need a letterhead and business card design for an Indian Pharmaceutical Export company.

The letter head needs to contain the following information.
Vorin Healthline Pvt. Ltd.
Office No 4827 Plot No 19, Larkspire, KT Lane, 400153, Maharashtra, India.
Email: info@vorin-healthline.com
Phone: +91-8342196507
CIN: U71853MH2025PTC902617
GSTIN: (This number is still pending, we will add later)

The business card needs to contain:
Address:
Vorin Healthline Pvt. Ltd.
Office No 4827 Plot No19, Larkspire, KT Lane, 400153, MH, India.
Email: torvald@vorin-healthline.com
Phone: +49-17634902851
Name on card: Torvald Ramming
Position: Director

The design for the letter head and business card should be simple but trustworthy.
Please use only Green and blue, same as in the attached logo.

```html
<!DOCTYPE html>
<html lang="en">
<head>
<meta charset="utf-8">
<title>Vorin Healthline Letterhead</title>
<link href="https://fonts.googleapis.com/css2?family=Montserrat:wght@500;600;700&family=Raleway:wght@400;500&family=Roboto:wght@400&display=swap" rel="stylesheet">
<style>
  :root {
    --blue: #1b75bb;
    --blue-dark: #0f5c9e;
    --green: #8dc63f;
    --ink: #222222;
    --muted: #555555;
    --paper: #ffffff;
    --backdrop: #e1e1e1;
  }
  html, body {
    margin: 0;
    width: 1200px;
    height: 1200px;
    overflow: hidden;
    background: var(--backdrop);
  }
  .stage { position: relative; width: 1200px; height: 1200px; }
  .letterhead {
    position: absolute;
    left: 216px;
    top: 76px;
    width: 1238px;
    height: 1684px;
    background: var(--paper);
    transform: scale(0.6211);
    transform-origin: 0 0;
    overflow: hidden;
    font-family: "Raleway", sans-serif;
    font-variant-numeric: lining-nums;
    color: var(--ink);
  }
  .brand-mark {
    position: absolute;
    left: 118px;
    top: 70px;
    width: 140px;
    height: 140px;
    border-radius: 50%;
    background: var(--blue);
  }
  .brand-name {
    position: absolute;
    left: 88px;
    top: 246px;
    width: 200px;
    text-align: center;
    font-family: "Montserrat", sans-serif;
    font-weight: 700;
    font-size: 22px;
    color: var(--blue-dark);
    white-space: nowrap;
  }
  .company-details {
    position: absolute;
    left: 851px;
    top: 92px;
    font-family: "Montserrat", sans-serif;
    font-size: 19px;
    line-height: 22px;
    color: var(--ink);
  }
  .company-details .company-name {
    font-weight: 600;
    font-size: 22px;
    color: var(--blue);
    margin: 0 0 2px;
  }
  .company-details p { margin: 0 0 0 2px; }
  .company-details .registration { margin-top: 20px; }
  .salutation {
    position: absolute;
    left: 86px;
    top: 388px;
    margin: 0;
    font-family: "Montserrat", sans-serif;
    font-weight: 600;
    font-size: 40px;
    color: var(--blue);
  }
  .letter-body {
    position: absolute;
    left: 88px;
    top: 468px;
    width: 1062px;
    font-size: 29.5px;
    line-height: 38.2px;
    text-align: justify;
    letter-spacing: -0.95px;
  }
  .letter-body p { margin: 0 0 38px; }
  .signatory {
    position: absolute;
    left: 100px;
    top: 1207px;
    font-family: "Roboto", sans-serif;
    color: var(--muted);
  }
  .signatory .name { font-size: 19px; margin: 0; }
  .signatory .role { font-size: 14px; margin: 4px 0 0; }
  .signature-area {
    position: absolute;
    left: 88px;
    top: 1260px;
    width: 280px;
    height: 125px;
    border-radius: 8px;
    background: linear-gradient(135deg, #f4f4f4, #ebebeb);
  }
  .contact {
    position: absolute;
    left: 758px;
    top: 1448px;
    font-family: "Raleway", sans-serif;
    font-size: 31px;
    line-height: 44px;
    color: var(--ink);
  }
  .contact-row { display: flex; align-items: center; gap: 10px; }
  .contact-row svg { width: 34px; height: 34px; flex: none; }
  .footer-band {
    position: absolute;
    left: 0;
    bottom: 0;
    width: 1238px;
    height: 96px;
    background: linear-gradient(90deg, var(--blue), var(--blue) 55%, var(--green));
  }
</style>
</head>
<body>
<div class="stage">
  <section class="letterhead">
    <div class="brand-mark"></div>
    <div class="brand-name">Vorin Healthline</div>

    <div class="company-details">
      <p class="company-name">Vorin Healthline Pvt. Ltd.</p>
      <p>Office No 4827 Plot No 19,<br>Larkspire, KT Lane, 400153,<br>Maharashtra, India.</p>
      <p class="registration">CIN: U71853MH2025PTC902617<br>GSTIN: 00000000</p>
    </div>

    <h1 class="salutation">Dear Mr. Arlen,</h1>

    <div class="letter-body">
      <p>Lorem ipsum dolor sit amet, consectetuer adipiscing elit, sed diam nonummy nibh euismod tincidunt ut laoreet dolore magna aliquam erat volutpat. Ut wisi enim ad minim veniam, quis nostrud exerci tation ullamcorper suscipit lobortis nisl ut aliquip ex ea commodo consequat. Duis autem vel eum iriure dolor in<br>&nbsp;hendrerit in vulputate velit esse molestie consequat, vel illum dolore eu feugiat nulla facilisis at vero eros et accumsan et iusto odio dignissim qui blandit praesent luptatum zzril delenit augue duis dolore te feugait nulla facilisi.</p>
      <p>Lorem ipsum dolor sit amet, cons ectetuer adipiscing elit, sed diam nonummy nibh euismod tincidunt ut laoreet dolore magna aliquam erat volutpat. Ut wisi Lorem ipsum dolor sit amet, consectetuer adipiscing elit, sed diam nonummy nibh euismod tincidunt ut laoreet dolore magna aliquam erat volutpat. Ut wisi enim ad minim veniam, quis nostrud exerci tation ullamcorper suscipit lobortis nisl ut aliquip ex ea commodo consequat. Duis autem vel eum iriure dolor in hendrerit in vulputate velit esse molestie consequat,Lorem ipsum dolor sit amet, cons ectetuer adipiscing elit, sed diam nonummy nibh euismod tincidunt ut laoreet dolore magna aliquam erat volutpat.</p>
    </div>

    <div class="signatory">
      <p class="name">Arlen Voss</p>
      <p class="role">Office Maneger</p>
    </div>
    <div class="signature-area" role="img" aria-label="Handwritten signature of the office manager"></div>

    <div class="contact">
      <div class="contact-row">
        <svg viewBox="0 0 24 24" aria-hidden="true"><path fill="#1b75bb" d="M6.6 10.8a15.1 15.1 0 0 0 6.6 6.6l2.2-2.2a1 1 0 0 1 1-.25 11.4 11.4 0 0 0 3.6.57 1 1 0 0 1 1 1V20a1 1 0 0 1-1 1A17 17 0 0 1 3 4a1 1 0 0 1 1-1h3.5a1 1 0 0 1 1 1c0 1.25.2 2.45.57 3.57a1 1 0 0 1-.25 1z"/></svg>
        <span>+91-8342196507</span>
      </div>
      <div class="contact-row">
        <svg viewBox="0 0 24 24" aria-hidden="true"><path fill="#1b75bb" d="M2 5h20v14H2z"/><path fill="none" stroke="#fff" stroke-width="1.6" d="M2.5 5.5 12 13l9.5-7.5M2.5 18.5l7-6.5M21.5 18.5l-7-6.5"/></svg>
        <span>info@vorin-healthline.com</span>
      </div>
    </div>

    <div class="footer-band" role="img" aria-label="Decorative blue and green footer band"></div>
  </section>
</div>
</body>
</html>
```